K & R Acreage Works. Business card design

We need a business card designed for a new business. We have a bulldozer and tractor service. We clear land and make wildlife food plots. We provide disking, bush hogging, and site prep services.
I have attached an image of a business card that I like and would like my business cards to look similar.

Target Market(s)

anyone needing bulldozer and/or tractor services

Industry/Entity Type

Business

Contact Information for Business Card

K & R Acreage Works, Operated by 7-M-Ranch
Doug Pelham
601-473-5826
dpr4178@mailvexo.com

Font styles to use
Sans Serif

Colors

Designer to choose colors to be used in the design.

Requirements
Must have
• image of tractor and bulldozer
• Land Clearing
• Wildlife food plots
• Bush Hogging
• Disking
• Site prep
Nice to have
• i have included a image of a business card that i like. I would like mine to be similar.

```html
<!DOCTYPE html>
<html lang="en">
<head>
<meta charset="utf-8">
<title>K &amp; R Acreage Works – Business Card</title>
<link rel="stylesheet" href="https://fonts.googleapis.com/css2?family=Kalam:wght@400;700&display=swap">
<style>
  :root{
    --page:#dcdcdc;
    --card-white:#f7f7f7;
    --card-black:#050505;
    --orange:#f0a000;
    --orange-deep:#e9861c;
    --ink:#111111;
    --white:#ffffff;
    --photo-top:#6d7a4a;
    --photo-bottom:#3f5a25;
  }
  *{box-sizing:border-box;margin:0;padding:0}
  html,body{width:1200px;height:900px;overflow:hidden;background:var(--page)}
  body{font-family:"Kalam",cursive;position:relative}
  .card{
    position:absolute;left:337px;width:525px;height:300px;
    border-radius:22px;overflow:hidden;
    box-shadow:0 6px 18px rgba(0,0,0,.25);
  }
  /* front */
  .card-front{top:110px;background:var(--card-white)}
  .photo{
    position:absolute;left:0;top:0;width:100%;height:142px;
    background:linear-gradient(180deg,var(--photo-top),var(--photo-bottom));
  }
  .photo-rule{position:absolute;left:0;top:142px;width:100%;height:6px;background:var(--orange)}
  .holder{position:absolute;left:36px;top:162px}
  .holder-name{font-weight:700;font-size:24px;letter-spacing:.5px;color:var(--ink);text-transform:uppercase;line-height:1}
  .holder-role{font-size:15px;color:var(--orange);text-transform:uppercase;line-height:1.2}
  .contacts{position:absolute;left:36px;top:210px;list-style:none}
  .contacts li{display:flex;align-items:center;gap:6px;font-size:15px;color:var(--ink);text-transform:uppercase;line-height:1.45;white-space:nowrap}
  .contacts svg{width:13px;height:13px;fill:var(--orange);flex:none}
  .brand{
    position:absolute;display:flex;align-items:center;gap:8px;
    font-weight:700;text-transform:uppercase;line-height:1;white-space:nowrap;
  }
  .brand-mark{width:14px;height:14px;background:var(--orange);flex:none}
  .card-front .brand{right:28px;bottom:18px;font-size:21px;color:var(--ink)}
  /* back */
  .card-back{top:480px;background:var(--card-black)}
  .services{position:absolute;left:40px;top:34px}
  .services-title{font-size:17px;color:var(--orange);text-transform:uppercase;margin-bottom:4px}
  .services-list{list-style:none}
  .services-list li{display:flex;align-items:center;gap:7px;font-size:17px;color:var(--white);text-transform:uppercase;line-height:1.55}
  .services-list svg{width:14px;height:14px}
  .card-back .brand{right:34px;bottom:40px;font-size:26px;color:var(--orange)}
  .card-back .brand-mark{width:18px;height:18px}
</style>
</head>
<body>
  <section class="card card-front">
    <div class="photo" role="img" aria-label="Photo of an orange tractor with front loader and a yellow bulldozer clearing brush in a wooded field"></div>
    <div class="photo-rule"></div>
    <div class="holder">
      <p class="holder-name">Doug Pelham</p>
      <p class="holder-role">Owner</p>
    </div>
    <ul class="contacts">
      <li><svg viewBox="0 0 24 24" aria-hidden="true"><path d="M6.6 10.8a15.1 15.1 0 0 0 6.6 6.6l2.2-2.2a1 1 0 0 1 1-.25 11.4 11.4 0 0 0 3.6.57 1 1 0 0 1 1 1V20a1 1 0 0 1-1 1A17 17 0 0 1 3 4a1 1 0 0 1 1-1h3.5a1 1 0 0 1 1 1c0 1.250.2 2.45.57 3.57a1 1 0 0 1-.25 1z"/></svg>601-473-5826</li>
      <li><svg viewBox="0 0 24 24" aria-hidden="true"><path d="M2 5h20v14H2z M2 5l10 8 10-8" stroke="#fff" stroke-width="1.5"/></svg>dpr4178@mailvexo.com</li>
    </ul>
    <div class="brand"><span class="brand-mark"></span>K &amp; R Acreage Works</div>
  </section>

  <section class="card card-back">
    <div class="services">
      <p class="services-title">Our Services</p>
      <ul class="services-list">
        <li><svg viewBox="0 0 16 16" aria-hidden="true"><rect x="1" y="3" width="11" height="11" fill="#f0a000"/><path d="M3 8l3 3 8-9" fill="none" stroke="#111" stroke-width="2"/></svg>Land Clearing</li>
        <li><svg viewBox="0 0 16 16" aria-hidden="true"><rect x="1" y="3" width="11" height="11" fill="#f0a000"/><path d="M3 8l3 3 8-9" fill="none" stroke="#111" stroke-width="2"/></svg>Wildlife Food Plots</li>
        <li><svg viewBox="0 0 16 16" aria-hidden="true"><rect x="1" y="3" width="11" height="11" fill="#f0a000"/><path d="M3 8l3 3 8-9" fill="none" stroke="#111" stroke-width="2"/></svg>Bush Hogging</li>
        <li><svg viewBox="0 0 16 16" aria-hidden="true"><rect x="1" y="3" width="11" height="11" fill="#f0a000"/><path d="M3 8l3 3 8-9" fill="none" stroke="#111" stroke-width="2"/></svg>Disking</li>
        <li><svg viewBox="0 0 16 16" aria-hidden="true"><rect x="1" y="3" width="11" height="11" fill="#f0a000"/><path d="M3 8l3 3 8-9" fill="none" stroke="#111" stroke-width="2"/></svg>Site Prep</li>
      </ul>
    </div>
    <div class="brand"><span class="brand-mark"></span>K &amp; R Acreage Works</div>
  </section>
</body>
</html>
```